Flyer for Commercial Roofing Company

We are seeking a talented graphic designer to create a high-quality, visually appealing bifold brochure for Tallbrook Roofing, a certified commercial roofing company specializing in apartment communities. The brochure will be 8.5x11 inches when folded and 17x11 inches when open, containing a front cover, two inside pages, and a back cover. The content is already developed, highlighting our services, key features, and contact information. The design should incorporate professional imagery of multifamily properties, modern icons, a clean layout, and our brand colors and logo to convey trust, expertise, and innovation. The goal is to produce a compelling marketing piece that engages property managers and decision-makers.
Target Market(s)
Apartment Communites
Look and feel
Each slider illustrates characteristics of the customer's brand and the style your logo design should communicate.

```html
<!DOCTYPE html>
<html lang="en">
<head>
<meta charset="utf-8">
<title>Tallbrook Roofing – Brochure Inside Spread</title>
<link href="https://fonts.googleapis.com/css2?family=Montserrat:wght@300;400;600;700;800&display=swap" rel="stylesheet">
<style>
  :root {
    --brand-red: #a32f35;
    --brand-red-dark: #92282e;
    --brand-navy: #3e3f91;
    --heading-navy: #33368f;
    --ink: #1d1d1f;
    --white: #ffffff;
  }
  * { margin: 0; padding: 0; box-sizing: border-box; }
  html, body { width: 1200px; height: 777px; overflow: hidden; background: var(--white); }
  body { font-family: "Montserrat", sans-serif; color: var(--white); }
  .spread { position: relative; width: 1200px; height: 777px; overflow: hidden; background: var(--white); }
  .backdrop { position: absolute; inset: 0; width: 1200px; height: 777px; }
  .block { position: absolute; }

  .intro { left: 65px; top: 30px; width: 500px; color: var(--ink); }
  .intro-title { font-size: 22.5px; font-weight: 800; color: var(--heading-navy); letter-spacing: 0.2px; margin-bottom: 11px; }
  .intro-text { font-size: 13.4px; font-weight: 600; line-height: 18.5px; }

  .section-title { font-size: 19px; font-weight: 700; letter-spacing: 0.2px; }

  .highlights { left: 64px; top: 187px; width: 250px; }
  .highlight-list { list-style: none; margin-top: 12px; }
  .highlight { position: relative; padding-left: 33px; margin-bottom: 12px; }
  .highlight svg { position: absolute; left: 1px; top: 2px; }
  .item-title { font-size: 12.6px; font-weight: 700; line-height: 15.5px; }
  .item-text { font-size: 12.8px; font-weight: 300; line-height: 16px; }

  .solutions { left: 64px; top: 474px; width: 470px; }
  .icon-list { list-style: none; }
  .icon-item { position: relative; padding-left: 54px; min-height: 33px; }
  .icon-item .icon { position: absolute; left: 1px; top: 0; }
  .solutions .icon-list { margin-top: 17px; }
  .solutions .icon-item { margin-bottom: 15px; }

  .services { left: 648px; top: 32px; width: 380px; }
  .services-intro { font-size: 12.6px; font-weight: 600; line-height: 15px; margin: 8px 0 12px; }
  .services .icon-item { padding-left: 45px; margin-bottom: 9px; }
  .services .icon-item .icon { left: -3px; }

  .brand { left: 963px; top: 671px; display: flex; align-items: center; gap: 12px; color: var(--brand-navy); }
  .brand-square { width: 16px; height: 16px; background: var(--brand-red); }
  .brand-name { font-size: 22px; font-weight: 800; letter-spacing: 0.6px; line-height: 1; }
</style>
</head>
<body>
<main class="spread">
  <svg class="backdrop" viewBox="0 0 1800 1165" preserveAspectRatio="none" aria-hidden="false">
    <defs>
      <linearGradient id="g-nailer" x1="0" y1="0" x2="1" y2="1">
        <stop offset="0" stop-color="#4f6a3a"/><stop offset="0.5" stop-color="#6b6f72"/><stop offset="1" stop-color="#8d9093"/>
      </linearGradient>
      <linearGradient id="g-membrane" x1="0" y1="0" x2="1" y2="1">
        <stop offset="0" stop-color="#3a3b3d"/><stop offset="0.55" stop-color="#8a4a3e"/><stop offset="1" stop-color="#a9b0b4"/>
      </linearGradient>
      <linearGradient id="g-roof" x1="0" y1="0" x2="1" y2="1">
        <stop offset="0" stop-color="#2e3036"/><stop offset="0.6" stop-color="#3b3e45"/><stop offset="1" stop-color="#d9cdb8"/>
      </linearGradient>
      <linearGradient id="g-coating" x1="0" y1="0" x2="0" y2="1">
        <stop offset="0" stop-color="#4a3c33"/><stop offset="0.5" stop-color="#8e8a80"/><stop offset="1" stop-color="#d8d9d8"/>
      </linearGradient>
    </defs>
    <polygon points="0,170 490,315 490,720 0,585" fill="var(--brand-red)"/>
    <polygon points="900,0 1800,0 1540,75 1540,410 900,600" fill="var(--brand-red)"/>
    <g role="img" aria-label="Photo: roofer fastening asphalt shingles with a nail gun">
      <polygon points="500,195 900,315 900,592 500,485" fill="url(#g-nailer)"/>
    </g>
    <g role="img" aria-label="Photo: roll of roofing membrane being laid on a flat roof">
      <polygon points="500,490 900,602 900,850 500,732" fill="url(#g-membrane)"/>
    </g>
    <g role="img" aria-label="Photo: worker applying white coating to a flat roof with a roller">
      <polygon points="1540,75 1800,0 1800,340 1540,410" fill="url(#g-coating)"/>
    </g>
    <g role="img" aria-label="Photo: aerial view of a flat apartment roof with vents and parapets">
      <polygon points="900,600 1800,340 1800,820 1290,965 900,850" fill="url(#g-roof)"/>
    </g>
    <polygon points="0,585 1290,965 620,1165 0,1165" fill="var(--brand-navy)"/>
  </svg>

  <section class="block intro">
    <h1 class="intro-title">Why Choose Tallbrook Roofing?</h1>
    <p class="intro-text">We specialize in delivering superior roofing services tailored to meet the needs of apartment communities. Our certified experts ensure your property's roof is built to last.</p>
  </section>

  <section class="block highlights">
    <h2 class="section-title">Key Highlights:</h2>
    <ul class="highlight-list">
      <li class="highlight">
        <svg width="16" height="13" viewBox="0 0 16 13"><path d="M1.5 7 L6 11 L14.5 1.5" fill="none" stroke="#fff" stroke-width="3" stroke-linecap="round" stroke-linejoin="round"/></svg>
        <div class="item-title">Certified Roofing Contractor:</div>
        <div class="item-text">Expert craftsmanship<br>guaranteed.</div>
      </li>
      <li class="highlight">
        <svg width="16" height="13" viewBox="0 0 16 13"><path d="M1.5 7 L6 11 L14.5 1.5" fill="none" stroke="#fff" stroke-width="3" stroke-linecap="round" stroke-linejoin="round"/></svg>
        <div class="item-title">20-Year NDL Warranty:</div>
        <div class="item-text">Peace of mind with long-term protection.</div>
      </li>
      <li class="highlight">
        <svg width="16" height="13" viewBox="0 0 16 13"><path d="M1.5 7 L6 11 L14.5 1.5" fill="none" stroke="#fff" stroke-width="3" stroke-linecap="round" stroke-linejoin="round"/></svg>
        <div class="item-title">Vendor Credentialing<br>Compliance:</div>
        <div class="item-text">Approved with all major<br>platforms.</div>
      </li>
    </ul>
  </section>

  <section class="block solutions">
    <h2 class="section-title">Roofing Solutions:</h2>
    <ul class="icon-list">
      <li class="icon-item">
        <svg class="icon" width="33" height="33" viewBox="0 0 33 33"><circle cx="16.5" cy="16.5" r="15.5" fill="#fff"/><g fill="none" stroke="var(--brand-navy)" stroke-width="1.4"><rect x="10" y="9" width="14" height="15" rx="1"/><circle cx="12" cy="21" r="3"/><line x1="15" y1="16" x2="24" y2="16"/></g></svg>
        <div class="item-title">TPO Roofing:</div>
        <div class="item-text">Energy-efficient and durable for large flat roofs.</div>
      </li>
      <li class="icon-item">
        <svg class="icon" width="33" height="33" viewBox="0 0 33 33"><circle cx="16.5" cy="16.5" r="15.5" fill="#fff"/><g fill="none" stroke="var(--brand-navy)" stroke-width="1.4"><path d="M9 22 L17 9 L24 12 L19 25 Z"/><circle cx="12" cy="21" r="2.5"/></g></svg>
        <div class="item-title">EPDM Roofing:</div>
        <div class="item-text">Resilient against extreme weather with proven longevity.</div>
      </li>
      <li class="icon-item">
        <svg class="icon" width="33" height="33" viewBox="0 0 33 33"><circle cx="16.5" cy="16.5" r="15.5" fill="#fff"/><g fill="none" stroke="var(--brand-navy)" stroke-width="1.4"><rect x="10" y="10" width="5" height="14" rx="1"/><rect x="15" y="16" width="9" height="8"/><circle cx="12.5" cy="21" r="1.5"/></g></svg>
        <div class="item-title">PVC Roofing:</div>
        <div class="item-text">Fire, chemical, and water-resistant for multifamily properties.</div>
      </li>
      <li class="icon-item">
        <svg class="icon" width="33" height="33" viewBox="0 0 33 33"><circle cx="16.5" cy="16.5" r="15.5" fill="#fff"/><g fill="none" stroke="var(--brand-navy)" stroke-width="1.3"><path d="M8 23 L14 10 L25 10 L19 23 Z"/><line x1="11" y1="17" x2="22" y2="17"/><line x1="16" y1="10" x2="11" y2="23"/><line x1="20" y1="10" x2="15" y2="23"/></g></svg>
        <div class="item-title">Asphalt Shingles:</div>
        <div class="item-text">Versatile and cost-effective with curb appeal.</div>
      </li>
      <li class="icon-item">
        <svg class="icon" width="33" height="33" viewBox="0 0 33 33"><circle cx="16.5" cy="16.5" r="15.5" fill="#fff"/><g fill="var(--brand-navy)"><rect x="9" y="9" width="14" height="6" rx="1"/><rect x="23" y="11" width="2" height="5"/><rect x="15" y="15" width="3" height="4"/><rect x="14" y="19" width="5" height="6" rx="1"/></g></svg>
        <div class="item-title">Roof Coatings:</div>
        <div class="item-text">Extend the lifespan of existing roofs and reduce<br>maintenance costs.</div>
      </li>
    </ul>
  </section>

  <section class="block services">
    <h2 class="section-title">Our Services</h2>
    <p class="services-intro">We offer comprehensive roofing solutions for every stage of your roof’s lifecycle.</p>
    <ul class="icon-list">
      <li class="icon-item">
        <svg class="icon" width="33" height="33" viewBox="0 0 33 33"><circle cx="16.5" cy="16.5" r="15.5" fill="#fff"/><g stroke="var(--brand-red)" stroke-width="2" stroke-linecap="round"><line x1="10" y1="10" x2="23" y2="23"/><line x1="23" y1="10" x2="10" y2="23"/></g></svg>
        <div class="item-title">Roof Repairs:</div>
        <div class="item-text">Fast, reliable fixes to extend roof life.</div>
      </li>
      <li class="icon-item">
        <svg class="icon" width="33" height="33" viewBox="0 0 33 33"><circle cx="16.5" cy="16.5" r="15.5" fill="#fff"/><g fill="none" stroke="var(--brand-red)" stroke-width="2" stroke-linecap="round"><circle cx="18.5" cy="14" r="5.5"/><line x1="14.5" y1="18" x2="9.5" y2="23"/></g></svg>
        <div class="item-title">Roof Inspections:</div>
        <div class="item-text">Thorough assessments to identify potential issues.</div>
      </li>
      <li class="icon-item">
        <svg class="icon" width="33" height="33" viewBox="0 0 33 33"><circle cx="16.5" cy="16.5" r="15.5" fill="#fff"/><g fill="none" stroke="var(--brand-red)" stroke-width="2"><circle cx="16.5" cy="16.5" r="6" stroke-dasharray="3 2"/><circle cx="16.5" cy="16.5" r="2.5"/></g></svg>
        <div class="item-title">Preventative Maintenance:</div>
        <div class="item-text">Keep your roof in optimal condition year-round.</div>
      </li>
      <li class="icon-item">
        <svg class="icon" width="33" height="33" viewBox="0 0 33 33"><circle cx="16.5" cy="16.5" r="15.5" fill="#fff"/><g fill="var(--brand-red)"><path d="M8 22 L25 16 L25 22 Z"/><rect x="13" y="12" width="4" height="6"/></g></svg>
        <div class="item-title">New Roof Installations:</div>
        <div class="item-text">High-quality installations with certified materials.</div>
      </li>
      <li class="icon-item">
        <svg class="icon" width="33" height="33" viewBox="0 0 33 33"><circle cx="16.5" cy="16.5" r="15.5" fill="#fff"/><circle cx="16.5" cy="16.5" r="10" fill="none" stroke="var(--brand-red)" stroke-width="1.6"/><text x="16.5" y="19.5" text-anchor="middle" font-family="Montserrat, sans-serif" font-size="7.5" font-weight="700" fill="var(--brand-red)">24/7</text></svg>
        <div class="item-title">Emergency Services:</div>
        <div class="item-text">24/7 rapid response to urgent<br>roofing issues.</div>
      </li>
    </ul>
  </section>

  <div class="block brand">
    <span class="brand-square"></span>
    <span class="brand-name">TALLBROOK<br>ROOFING</span>
  </div>
</main>
</body>
</html>
```